Brochure required for large legal practice

We require a brochure, poster and PowerPoint to be designed to promote our new Employee Benefits Program to our employees. The brochure needs to be modern, clean and corporate. Our target market is solicitors, legal support staff and administration staff based across multiple sites in Queensland, Australia. Logos and brochure/poster content have been attached as well as a detailed brief.

Please note that several photos of our employees have now been uploaded and can be used in this material only.                             

Legal

```html
<!DOCTYPE html>
<html lang="en">
<head>
<meta charset="utf-8">
<title>Norvale Group – Employee Benefits Program Brochure</title>
<link rel="stylesheet" href="https://fonts.googleapis.com/css2?family=Arimo:wght@400;700&family=Open+Sans:wght@400&display=swap">
<style>
  :root {
    --backdrop: #d9d6d0;
    --paper: #ffffff;
    --spine: #231f20;
    --stone: #7b7a71;
    --stone-light: #a8a9a4;
    --stone-mid: #8b8b83;
    --ink: #1f1f1f;
    --mark: #6f6f68;
    --photo-warm-a: #e4e0dc;
    --photo-warm-b: #a97a5c;
    --photo-dark-a: #1d2230;
    --photo-dark-b: #d2a890;
  }
  * { box-sizing: border-box; margin: 0; padding: 0; }
  html, body { width: 1200px; height: 870px; overflow: hidden; }
  body {
    position: relative;
    background: var(--backdrop);
    font-family: "Arimo", Arial, sans-serif;
  }
  .panel { position: absolute; top: 35px; height: 798px; background: var(--paper); }
  .panel--back { left: 35px; width: 379px; }
  .panel--spine { left: 414px; width: 186px; background: var(--spine); }
  .panel--cover { left: 600px; width: 564px; }

  /* back panel */
  .back-photo {
    position: absolute; left: 0; top: 17px; width: 379px; height: 281px;
    background: linear-gradient(100deg, var(--photo-warm-a) 0%, var(--photo-warm-b) 45%, var(--photo-warm-a) 100%);
  }
  .philosophy {
    position: absolute; left: 0; top: 305px; width: 379px; height: 275px;
    background: var(--stone);
  }
  .philosophy__tag { position: absolute; left: 17px; top: 10px; }
  .philosophy__title {
    position: absolute; left: 27px; top: 15px;
    font-size: 14.5px; color: #fff; letter-spacing: -0.3px;
  }
  .philosophy__list {
    position: absolute; left: 23px; top: 58px; width: 315px;
    list-style: none; font-size: 10.4px; line-height: 13px; color: var(--ink);
    letter-spacing: -0.1px;
  }
  .philosophy__list li { margin-bottom: 10px; padding-left: 7px; text-indent: -7px; }
  .philosophy__list li::before { content: "\2022"; margin-right: 2px; }

  .brand {
    display: flex; align-items: center; gap: 10px;
    color: var(--mark); font-family: "Arimo", Arial, sans-serif; font-weight: 400;
  }
  .brand__square { flex: none; background: var(--mark); }
  .brand__name { display: flex; flex-direction: column; }
  .brand--back { position: absolute; left: 118px; top: 633px; font-size: 20px; line-height: 22px; }
  .brand--back .brand__square { width: 26px; height: 26px; }
  .contact {
    position: absolute; left: 13px; top: 722px; width: 366px; text-align: center;
    font-family: "Open Sans", Arial, sans-serif; font-size: 21.5px; line-height: 28px; color: var(--ink);
  }

  /* cover panel */
  .brand--cover { position: absolute; left: 14px; top: 20px; font-size: 27px; line-height: 32px; }
  .brand--cover .brand__square { width: 34px; height: 34px; }
  .cover-strip { position: absolute; left: 208px; top: 0; width: 38px; height: 265px; background: var(--stone-mid); }
  .cover-strip--top { left: 208px; width: 356px; height: 17px; }
  .slogan {
    position: absolute; left: 246px; top: 17px; width: 318px; height: 248px;
    background: var(--stone-light);
    padding: 52px 18px 0 0; text-align: right;
    font-size: 23.5px; line-height: 49px; color: #fff; letter-spacing: -0.6px;
  }
  .cover-photo {
    position: absolute; left: 0; top: 267px; width: 564px; height: 431px;
    background: radial-gradient(ellipse at 60% 65%, var(--photo-dark-b) 0%, #6b5a55 35%, var(--photo-dark-a) 75%);
  }
  .cover-foot { position: absolute; left: 0; top: 698px; width: 187px; height: 100px; background: var(--stone); }
  .cover-foot-rule { position: absolute; left: 187px; top: 700px; width: 377px; height: 11px; background: var(--stone-light); }
  .cover-title {
    position: absolute; left: 193px; top: 724px;
    font-size: 21px; font-weight: 400; color: var(--mark); letter-spacing: -0.4px;
  }
</style>
</head>
<body>
  <section class="panel panel--back">
    <div class="back-photo" role="img" aria-label="Photo of two businesspeople shaking hands"></div>
    <div class="philosophy">
      <svg class="philosophy__tag" width="215" height="27" viewBox="0 0 215 27" aria-hidden="true">
        <polygon points="0,0 170,0 150,27 0,27" fill="#2a2a2a"/>
        <polygon points="178,0 215,0 195,27 158,27" fill="#b5b5ae"/>
      </svg>
      <span class="philosophy__title">Our philosophy we will</span>
      <ul class="philosophy__list">
        <li>Always listen to you properly</li>
        <li>Speak to you in plain English so you know exactly where you stand.</li>
        <li>Explain to you clearly and upfront, how much you will need to invest in any service you require help with.</li>
        <li>Ensure that there is a certainty of exactly what it is we are to do for you and always confirm that in writing.</li>
        <li>Ensure you know how long the work we are to do for you should take.</li>
        <li>Always explain what is involved and how things work.</li>
        <li>Keep you informed every step of the way.</li>
      </ul>
    </div>
    <div class="brand brand--back"><span class="brand__square"></span><span class="brand__name"><span>Norvale</span><span>Group</span></span></div>
    <p class="contact">Put your contact information and<br>address here</p>
  </section>

  <section class="panel panel--spine"></section>

  <section class="panel panel--cover">
    <div class="brand brand--cover"><span class="brand__square"></span><span class="brand__name"><span>Norvale</span><span>Group</span></span></div>
    <div class="cover-strip"></div>
    <div class="cover-strip cover-strip--top"></div>
    <div class="slogan">
      Wherever you work.<br>Whatever you do.<br>Whatever your need.<br>We're already there.
    </div>
    <div class="cover-photo" role="img" aria-label="Photo of several hands joining white puzzle pieces together"></div>
    <div class="cover-foot"></div>
    <div class="cover-foot-rule"></div>
    <h1 class="cover-title">Employee Benefits Program</h1>
  </section>
</body>
</html>
```